Harbor Compass - Book Cover

I need a book cover for my debut work, "Harbor Compass - Turning the Tide, One Step at a Time." While the website isn't complete, you can get a sense of what I am writing about by looking at my website, harborcompassbooks.org. The book is a leadership development book, but more of a personal change journey. The emphasis is on figuring out how to combine you work, social, and own self into an authentic package that not only resonates with others, but makes what you achieve more fulfilling.

I am attaching a copy of my logo so you can get a sense of what I like. I would prefer to not have the cover be photographic, but am open to suggestions. This will be a series of books so maintaining some sense of style will be important, and can garner future work.

Industry/Entity Type

Leadership

```html
<!DOCTYPE html>
<html lang="en">
<head>
<meta charset="utf-8">
<title>Harbor Compass – Book Cover</title>
<link rel="stylesheet" href="https://fonts.googleapis.com/css2?family=Jost:wght@400;500&display=swap">
<style>
  :root {
    --page-bg: #f1f1f1;
    --cover-green: #99b23d;
    --cover-dark: #232323;
    --divider: #ffffff;
    --title-white: #ffffff;
    --ink: #1e1e1e;
    --mark-blue: #0d4fa3;
  }
  html, body {
    margin: 0;
    padding: 0;
    width: 1200px;
    height: 1000px;
    overflow: hidden;
    background: var(--page-bg);
    font-family: "Jost", "Helvetica Neue", Arial, sans-serif;
  }
  .canvas {
    position: relative;
    width: 1200px;
    height: 1000px;
  }
  .book-cover {
    position: absolute;
    left: 431px;
    top: 262px;
    width: 338px;
    height: 477px;
    background: var(--cover-green);
    overflow: hidden;
  }
  .cover-band {
    position: absolute;
    left: 0;
    right: 0;
    top: 320px;
    bottom: 0;
    background: var(--cover-dark);
    border-top: 8px solid var(--divider);
  }
  .cover-text {
    position: absolute;
    left: 42px;
    top: 42px;
  }
  .author-name {
    margin: 0 0 12px 2px;
    font-size: 10px;
    font-weight: 500;
    letter-spacing: 0.04em;
    text-transform: uppercase;
    color: var(--ink);
  }
  .book-title {
    margin: 0;
    font-size: 32px;
    font-weight: 400;
    line-height: 1.1;
    color: var(--title-white);
  }
  .book-subtitle {
    margin: 4px 0 0;
    font-size: 17px;
    font-weight: 400;
    line-height: 1.25;
    color: var(--ink);
  }
  .series-disc {
    position: absolute;
    left: 164px;
    top: 296px;
    width: 220px;
    height: 220px;
    display: block;
  }
  .series-name {
    position: absolute;
    left: 22px;
    bottom: 34px;
    font-size: 16px;
    font-weight: 500;
    letter-spacing: 0.02em;
    color: var(--title-white);
  }
</style>
</head>
<body>
  <main class="canvas">
    <article class="book-cover">
      <div class="cover-band"></div>
      <header class="cover-text">
        <p class="author-name">Author's Name</p>
        <h1 class="book-title">Harbor Compass</h1>
        <p class="book-subtitle">Turning the Tide,<br>One Step at a Time.</p>
      </header>
      <svg class="series-disc" viewBox="0 0 220 220" aria-hidden="true">
        <circle cx="110" cy="110" r="110" fill="var(--mark-blue)"/>
      </svg>
      <span class="series-name">Harbor Compass</span>
    </article>
  </main>
</body>
</html>
```